TRV business card

Need a business card for a company that provides instructional design and elearning development services. The website is here: http://tarvexa.studio/

I'm attaching a current logo, as well as the old business card design. While I like to keep it clean, the old design is too simplistic for my liking. The only idea I want to reuse from the old design is placing industry jargon on the back of the card, just need a better way to present it. But if you have other ideas for the back--feel free to experiment.

Please use the colors complementary to the color we have on the website. Thank you!

```html
<!DOCTYPE html>
<html lang="en">
<head>
<meta charset="utf-8">
<title>TRV business card</title>
<link href="https://fonts.googleapis.com/css2?family=Jost:wght@500;600&family=Roboto+Condensed:wght@700&family=Roboto:wght@400&display=swap" rel="stylesheet">
<style>
  :root {
    --backdrop: #a9a7a7;
    --card-dark: #2b2b2d;
    --card-light: #f7f7f6;
    --teal: #19b29c;
    --teal-band: #16ae9a;
    --gold: #d6cb8c;
    --white: #ffffff;
    --ink: #2a2a2a;
    --ink-soft: #3a3a3a;
  }
  * { margin: 0; padding: 0; box-sizing: border-box; }
  html, body {
    width: 1200px; height: 1200px; overflow: hidden;
    background: var(--backdrop);
  }
  .card {
    position: absolute;
    overflow: hidden;
  }
  .card--front {
    left: 238px; top: 117px; width: 714px; height: 420px;
    border-radius: 24px;
    background: var(--card-dark);
  }
  .card--front svg { display: block; }
  .jargon {
    font-family: "Jost", sans-serif;
    font-weight: 600;
    font-size: 42px;
    fill: var(--teal);
  }
  .tagline {
    font-family: "Roboto Condensed", sans-serif;
    font-weight: 700;
    font-size: 76px;
    letter-spacing: -4px;
    fill: var(--white);
  }
  .tagline-bar { fill: var(--white); }

  .card--back {
    left: 231px; top: 644px; width: 711px; height: 416px;
    border-radius: 28px;
    background: var(--card-light);
  }
  .edge-band {
    position: absolute; left: 0; top: 0; bottom: 0; width: 60px;
    background: var(--teal-band);
  }
  .edge-line {
    position: absolute; left: 60px; top: 0; bottom: 0; width: 7px;
    background: var(--gold);
  }
  .brand {
    position: absolute; left: 112px; top: 62px;
    display: flex; align-items: center; gap: 14px;
  }
  .brand-dot {
    width: 22px; height: 22px; border-radius: 50%;
    background: var(--teal);
  }
  .brand-name {
    font-family: "Jost", sans-serif;
    font-weight: 600;
    font-size: 46px;
    color: var(--teal);
    letter-spacing: 0.5px;
  }
  .holder-name {
    position: absolute; left: 112px; top: 232px;
    font-family: "Jost", sans-serif;
    font-weight: 500;
    font-size: 24px;
    color: var(--ink);
  }
  .contact-list {
    position: absolute; left: 112px; top: 286px;
    list-style: none;
    font-family: "Roboto", sans-serif;
    font-size: 17px;
    color: var(--ink-soft);
  }
  .contact-list li {
    display: flex; align-items: center;
    height: 27px;
  }
  .contact-icon {
    width: 16px; height: 16px; margin-right: 18px;
    fill: var(--teal); stroke: var(--teal);
  }
</style>
</head>
<body>

<section class="card card--front" aria-label="Card front">
  <svg width="714" height="420" viewBox="0 0 714 420">
    <text class="jargon" x="42" y="58" textLength="630" lengthAdjust="spacing">MOBILE LEARNING SCORM</text>
    <text class="jargon" x="42" y="111" textLength="630" lengthAdjust="spacing">INSTRUCTIONAL DESIGN LMS</text>
    <text class="jargon" x="42" y="165" textLength="630" lengthAdjust="spacing">MOOCS ELEARNING HTML5</text>
    <rect class="tagline-bar" x="0" y="181" width="30" height="58"/>
    <text class="tagline" x="42" y="238" textLength="630" lengthAdjust="spacingAndGlyphs">HOW CAN WE HELP?</text>
    <rect class="tagline-bar" x="690" y="181" width="24" height="58"/>
    <text class="jargon" x="42" y="285" textLength="632" lengthAdjust="spacing">ADULT LEARNING THEORY</text>
    <text class="jargon" x="42" y="339" textLength="632" lengthAdjust="spacing">GAMIFICATION CLASSROOM</text>
    <text class="jargon" x="42" y="393" textLength="636" lengthAdjust="spacing">XAPI BLENDED LEARNING</text>
  </svg>
</section>

<section class="card card--back" aria-label="Card back">
  <div class="edge-band"></div>
  <div class="edge-line"></div>

  <div class="brand">
    <span class="brand-dot"></span>
    <span class="brand-name">Tarvexa Studio</span>
  </div>

  <p class="holder-name">Marcus Delahaye</p>

  <ul class="contact-list">
    <li>
      <svg class="contact-icon" viewBox="0 0 16 16" aria-hidden="true"><path stroke="none" d="M1 6c0-2 3-3 7-3s7 1 7 3v1h-3V5.5H4V7H1zM4 8h8l2 6H2z"/></svg>
      646-555-0182
    </li>
    <li>
      <svg class="contact-icon" viewBox="0 0 16 16" aria-hidden="true"><g fill="none" stroke-width="1.4"><circle cx="8" cy="8" r="6.5"/><ellipse cx="8" cy="8" rx="3" ry="6.5"/><line x1="1.5" y1="8" x2="14.5" y2="8"/></g></svg>
      www.tarvexa.studio
    </li>
    <li>
      <svg class="contact-icon" viewBox="0 0 16 16" aria-hidden="true"><rect stroke="none" x="1" y="3" width="14" height="10"/><path fill="none" stroke="#f7f7f6" stroke-width="1.3" d="M1.5 3.5L8 9l6.5-5.5M1.5 12.5l5-4.5M14.5 12.5l-5-4.5"/></svg>
      mdelahaye@tarvexa.studio
    </li>
  </ul>
</section>

</body>
</html>
```